Upsell Vertical Banner Ad Design For B2B Marketing Agency Vertical 768px × 1180px IS THE SIZE

I need a banner made for my website www.brightlanepromotionhub.biz This banner will be an upsell advertisement for after someone signs up for my monthly program. When they login to their account for the 1st time I will give them the chance to upgrade their account to our annual program with just one click.

this is a page that upsells it currently to give you an idea how we market ourselves:
https://tlpx.pagevault-example.com/page/tlp-annual-upsell

Use this content:

Are You Ready To Commit To Taking Your Business To The Next Level?

Because We're In This For The Long-Haul and Dedicated To Your Success...

Save $300 By Upgrading To An Annual Membership And Pay Only $74/mth

((BUTTON))Yes, Upgrade My Plan Right Now!

*Must prepay the full year at only $898/yr!

Target Market(s)

business owners

Industry/Entity Type

Marketing

Requirements
Must have
• 768px × 1180px IS THE SIZE vertical

Use this content:

Nice to have
• Use this content:

Should not have
• Use this content:

```html
<!DOCTYPE html>
<html lang="en">
<head>
<meta charset="utf-8">
<title>Annual Membership Upgrade – Bright Lane Promotion Hub</title>
<link href="https://fonts.googleapis.com/css2?family=Montserrat:ital,wght@0,400;0,500;0,700;0,800;0,900;1,900&display=swap" rel="stylesheet">
<style>
  :root {
    --red: #cc0a0a;
    --red-bright: #ee1c1c;
    --yellow: #ffd800;
    --button-yellow: #f9c300;
    --blue: #0b5fa8;
    --green: #4caf50;
    --green-dark: #3d9442;
    --ink: #111111;
    --white: #ffffff;
    --side-grey: #e2e2e2;
    --floor-grey: #c6c6c6;
  }
  * { margin: 0; padding: 0; box-sizing: border-box; }
  html, body { width: 781px; height: 1200px; overflow: hidden; background: var(--white); }
  .banner {
    position: relative;
    width: 781px;
    height: 1200px;
    overflow: hidden;
    background: var(--white);
    font-family: "Montserrat", Arial, sans-serif;
    color: var(--ink);
    text-align: center;
  }
  .side-panel {
    position: absolute;
    top: 183px;
    width: 31px;
    height: 840px;
    background: var(--side-grey);
  }
  .side-panel--left { left: 0; border-radius: 0 14px 14px 0; }
  .side-panel--right { right: 0; border-radius: 14px 0 0 14px; }
  .floor {
    position: absolute;
    left: 0; right: 0; bottom: 0;
    height: 108px;
    background: linear-gradient(#d6d6d6, var(--floor-grey));
  }
  .floor-glow {
    position: absolute;
    left: 0; right: 0;
    top: 1040px;
    height: 70px;
    background: linear-gradient(rgba(255,255,255,0), #ececec);
  }
  .top-band {
    position: absolute;
    left: 0; top: 0;
    width: 781px; height: 110px;
    background: var(--red);
    box-shadow: 0 4px 6px rgba(0,0,0,.25);
  }
  .top-band__title {
    position: absolute;
    left: 0; right: 0; top: 22px;
    font-size: 52px;
    font-weight: 800;
    color: var(--white);
    letter-spacing: 1px;
  }
  .qmark {
    position: absolute;
    font-weight: 900;
    line-height: 1;
  }
  .qmark--yellow { color: var(--yellow); }
  .qmark--red { color: var(--red-bright); }
  .qmark--a { left: 70px; top: 26px; font-size: 62px; transform: rotate(-8deg); }
  .qmark--b { left: 650px; top: 50px; font-size: 96px; transform: rotate(10deg); }
  .qmark--c { left: -14px; top: -8px; font-size: 56px; }
  .qmark--d { left: 745px; top: -4px; font-size: 70px; transform: rotate(8deg); }
  .lead {
    position: absolute; left: 0; right: 0; top: 163px;
    font-size: 24px; font-weight: 500;
  }
  .headline {
    position: absolute; left: 0; right: 0; top: 190px;
    font-size: 66px; font-weight: 800; color: var(--blue);
    letter-spacing: -0.5px;
  }
  .promise {
    position: absolute; left: 0; right: 0; top: 322px;
    font-size: 34px; font-weight: 500; line-height: 44px;
  }
  .save-tag {
    position: absolute; left: 156px; top: 498px;
    width: 468px; height: 112px;
  }
  .save-tag svg { position: absolute; inset: 0; }
  .save-tag__text {
    position: relative;
    padding-top: 14px;
    font-size: 68px; font-weight: 800; color: var(--white);
    text-shadow: 0 3px 4px rgba(0,0,0,.3);
  }
  .offer {
    position: absolute; left: 0; right: 0; top: 678px;
    font-size: 36px; font-weight: 500; line-height: 44px;
  }
  .offer__highlight {
    display: block;
    font-size: 50px; font-weight: 900; color: var(--blue);
    letter-spacing: 0.5px; line-height: 46px;
  }
  .terms {
    position: absolute; left: 122px; top: 866px;
    width: 536px; height: 41px;
    background: #000;
    border-radius: 8px;
    color: var(--white);
    font-size: 18px; font-weight: 500;
    line-height: 41px;
  }
  .cta {
    position: absolute; left: 90px; top: 953px;
    width: 598px; height: 128px;
    display: block; text-decoration: none;
  }
  .cta svg { position: absolute; inset: 0; }
  .cta__text {
    position: relative;
    padding-top: 10px;
    color: var(--red-bright);
    font-weight: 800;
  }
  .cta__line1 { display: block; font-size: 40px; line-height: 50px; }
  .cta__line2 { display: block; font-size: 54px; font-weight: 900; line-height: 56px; }
  .brand {
    position: absolute; left: 0; right: 0; top: 1126px;
    display: flex; align-items: center; justify-content: center; gap: 12px;
  }
  .brand__dot {
    width: 30px; height: 30px; border-radius: 50%;
    background: var(--blue);
  }
  .brand__name {
    font-size: 24px; font-weight: 700; color: var(--blue);
    letter-spacing: 1px; text-transform: uppercase;
  }
</style>
</head>
<body>
<main class="banner">
  <div class="side-panel side-panel--left"></div>
  <div class="side-panel side-panel--right"></div>
  <div class="floor-glow"></div>
  <div class="floor"></div>

  <header class="top-band">
    <span class="qmark qmark--red qmark--c">?</span>
    <span class="qmark qmark--red qmark--d">?</span>
    <span class="qmark qmark--yellow qmark--a">?</span>
    <h1 class="top-band__title">ARE YOU READY</h1>
  </header>
  <span class="qmark qmark--yellow qmark--b">?</span>

  <p class="lead">To commit to taking your business to</p>
  <h2 class="headline">The Next Level?</h2>
  <p class="promise">Because We're In This For The<br>Long-Haul and Dedicated To<br>Your Success...</p>

  <div class="save-tag">
    <svg width="468" height="112" viewBox="0 0 468 112">
      <polygon points="0,14 234,110 468,14 468,98 234,112 0,98" fill="rgba(0,0,0,.12)"/>
      <polygon points="6,0 462,0 456,88 234,104 12,88" fill="var(--green)"/>
    </svg>
    <p class="save-tag__text">SAVE $300</p>
  </div>

  <p class="offer">BY UPGRADING TO AN<span class="offer__highlight">ANNUAL MEMBERSHIP</span>AND PAY ONLY $74/MTH</p>

  <p class="terms">*MUST PREPAY THE FULL YEAR AT ONLY $898/YR!</p>

  <a class="cta" href="#upgrade">
    <svg width="598" height="128" viewBox="0 0 598 128">
      <polygon points="4,6 594,0 586,112 300,124 12,112" fill="rgba(0,0,0,.15)"/>
      <polygon points="0,0 598,0 590,106 300,118 8,106" fill="var(--button-yellow)"/>
    </svg>
    <span class="cta__text">
      <span class="cta__line1">YES, UPGRADE MY PLAN</span>
      <span class="cta__line2">RIGHT NOW!</span>
    </span>
  </a>

  <footer class="brand">
    <span class="brand__dot"></span>
    <span class="brand__name">Bright Lane Promotion Hub</span>
  </footer>
</main>
</body>
</html>
```